Vantrell Law Letterhead

We need a new letterhead design for a Law Firm. The address for the law firm is 4817 Larkspur Boulevard, Suite 250, Houston, Texas 77342. Phone Number: 832-619-3057; Fax Number: 832-407-1694. The logo is uploaded to the project.

```html
<!DOCTYPE html>
<html lang="en">
<head>
<meta charset="UTF-8">
<title>Vantrell Law Letterhead</title>
<link href="https://fonts.googleapis.com/css2?family=Cinzel:wght@600&family=Poppins:wght@400&display=swap" rel="stylesheet">
<style>
  :root {
    --navy: #1b2a55;
    --red: #d71f27;
    --band-light: #f2f2f2;
    --band-mid: #dcdddf;
    --band-deep: #d4d5d8;
    --footer: #dedfe1;
    --ink: #111111;
    --mark-tint: #f3f4f6;
    --paper: #ffffff;
  }
  html, body {
    margin: 0;
    padding: 0;
    overflow: hidden;
    background: var(--paper);
  }
  .letterhead {
    position: relative;
    width: 848px;
    height: 1200px;
    overflow: hidden;
    background: var(--paper);
    box-sizing: border-box;
    border: 1.5px solid var(--navy);
  }
  .header-bands,
  .backdrop-mark {
    position: absolute;
    left: 0;
    top: 0;
  }
  .brand {
    position: absolute;
    left: 53px;
    top: 62px;
    display: flex;
    align-items: center;
    gap: 14px;
  }
  .brand-dot {
    width: 56px;
    height: 56px;
    border-radius: 50%;
    background: var(--navy);
  }
  .brand-name {
    font-family: "Cinzel", serif;
    font-weight: 600;
    font-size: 34px;
    letter-spacing: 0.5px;
    color: var(--navy);
    margin: 0;
  }
  .contact {
    position: absolute;
    right: 47px;
    top: 68px;
    font-family: "Poppins", sans-serif;
    font-size: 22px;
    color: var(--ink);
    list-style: none;
    margin: 0;
    padding: 0;
  }
  .contact-line {
    display: flex;
    align-items: center;
    gap: 16px;
    height: 26px;
  }
  .contact-icon {
    width: 18px;
    height: 18px;
    flex: none;
  }
  .footer-band {
    position: absolute;
    left: 0;
    bottom: 0;
    width: 100%;
    height: 72px;
    background: var(--footer);
    display: flex;
    align-items: center;
    justify-content: center;
    font-family: "Poppins", sans-serif;
    font-size: 21px;
    color: var(--ink);
  }
</style>
</head>
<body>
<main class="letterhead">
  <svg class="header-bands" width="848" height="260" viewBox="0 0 848 260" aria-hidden="true">
    <polygon points="0,0 848,0 0,250" fill="var(--band-light)"/>
    <polygon points="248,0 848,0 848,208" fill="var(--band-mid)"/>
    <polygon points="248,0 848,0 523.7,95.6" fill="var(--band-deep)"/>
  </svg>

  <svg class="backdrop-mark" width="848" height="1200" viewBox="0 0 848 1200" aria-hidden="true">
    <circle cx="456" cy="650" r="245" fill="var(--mark-tint)"/>
  </svg>

  <header class="brand">
    <span class="brand-dot" aria-hidden="true"></span>
    <h1 class="brand-name">Vantrell Law</h1>
  </header>

  <ul class="contact">
    <li class="contact-line">
      <svg class="contact-icon" viewBox="0 0 20 20" aria-label="Phone">
        <circle cx="10" cy="10" r="9" fill="none" stroke="var(--navy)" stroke-width="1.2"/>
        <path d="M6.5 5.5l2 -0.5 1 2.5 -1.2 1a6 6 0 0 0 3 3l1-1.2 2.5 1 -0.5 2c-4 0.5 -8.5 -4 -7.8 -7.8z" fill="var(--navy)"/>
      </svg>
      <span>832-619-3057</span>
    </li>
    <li class="contact-line">
      <svg class="contact-icon" viewBox="0 0 20 20" aria-label="Fax">
        <rect x="6" y="2" width="7" height="7" fill="none" stroke="var(--navy)" stroke-width="1.2"/>
        <rect x="4" y="9" width="14" height="8" rx="1" fill="none" stroke="var(--navy)" stroke-width="1.2"/>
        <rect x="1" y="11" width="2.5" height="6" rx="0.8" fill="none" stroke="var(--navy)" stroke-width="1.2"/>
        <line x1="7" y1="13" x2="15" y2="13" stroke="var(--navy)" stroke-width="1.2"/>
      </svg>
      <span>832-407-1694</span>
    </li>
  </ul>

  <footer class="footer-band">
    4817 Larkspur Boulevard, Suite 250, Houston, Texas 77342
  </footer>
</main>
</body>
</html>
```